Real Estate Development Sign

I am trying to get some good graphic design help for a new real estate development project. We need two designs for two separate large billboard-type directionals, also For Sale Signs, and also bandit directional signs. I have a company who have already given it a shot, but I don't like what they have come up with. I need it to have a WOW factor and pop to catch people's eye, but also simple and easy to read. I've attached what they have done so far. I have proofs of what has already been created and I've attached them. I've also attached the logo for the project, but I'm fine with changing the color for the logo to help make the overall signs more cohesive. I want clean, easy to read and eye catching. I will need to be able to pass the designs on to a company to have them printed for the billboards. One of them is 10x12 and the other is 8x10. Time is of the essence - I've spent too much time trying to get this other company to do what I want.
Updates

Project Deadline Extended
Reason: Need more submissions.

I would like to shoot for Black, Red, White and a touch of Yellow for the colors of the signs.

Industry/Entity Type

Graphic Design

```html
<!DOCTYPE html>
<html lang="en">
<head>
<meta charset="utf-8">
<title>The Grove at Tarrowind Village – Open House Sign</title>
<link rel="stylesheet" href="https://fonts.googleapis.com/css2?family=Montserrat:wght@600&family=Oswald:wght@600&display=swap">
<style>
  :root {
    --backdrop: #e8e5e0;
    --frame-green: #2fa83a;
    --sign-white: #ffffff;
    --ink-brown: #3a1a16;
    --arrow-red: #ff0b0b;
    --label-yellow: #f6ee3a;
  }
  * { margin: 0; padding: 0; box-sizing: border-box; }
  html, body {
    width: 1200px;
    height: 960px;
    overflow: hidden;
    background: var(--backdrop);
  }
  .canvas {
    position: relative;
    width: 1200px;
    height: 960px;
  }
  .sign {
    position: absolute;
    left: 120px;
    top: 94px;
    width: 966px;
    height: 772px;
    background: var(--sign-white);
    border: 14px solid var(--frame-green);
  }
  .project-name {
    position: absolute;
    left: 0;
    right: 0;
    top: 84px;
    display: flex;
    justify-content: center;
    align-items: center;
    gap: 24px;
  }
  .project-dot {
    width: 34px;
    height: 34px;
    border-radius: 50%;
    background: var(--frame-green);
    flex: none;
  }
  .project-title {
    font-family: "Montserrat", sans-serif;
    font-weight: 600;
    color: var(--ink-brown);
    text-align: center;
    line-height: 1.05;
    letter-spacing: 2px;
  }
  .project-title .main { display: block; font-size: 124px; }
  .project-title .sub { display: block; font-size: 38px; letter-spacing: 4px; margin-top: 16px; }
  .direction-arrow {
    position: absolute;
    left: 0;
    top: 0;
    width: 966px;
    height: 772px;
  }
  .arrow-shape { fill: var(--arrow-red); }
  .arrow-label {
    font-family: "Oswald", sans-serif;
    font-weight: 600;
    font-size: 120px;
    fill: var(--label-yellow);
    letter-spacing: 2px;
  }
  .builder-name {
    position: absolute;
    left: 226px;
    top: 660px;
    font-family: "Montserrat", sans-serif;
    font-weight: 600;
    font-size: 32px;
    letter-spacing: 1.5px;
    color: var(--ink-brown);
  }
</style>
</head>
<body>
  <main class="canvas">
    <section class="sign">
      <div class="project-name">
        <span class="project-dot"></span>
        <h1 class="project-title">
          <span class="main">The Grove</span>
          <span class="sub">AT TARROWIND VILLAGE</span>
        </h1>
      </div>

      <svg class="direction-arrow" viewBox="0 0 966 772">
        <polygon class="arrow-shape"
                 points="76,434 628,434 628,378 884,530 628,684 628,626 76,626"/>
        <text class="arrow-label" x="112" y="574">OPEN HOUSE</text>
      </svg>

      <p class="builder-name">QUELLMOOR HOMES</p>
    </section>
  </main>
</body>
</html>
```